Business Card Design

we are a brand new cable TV network devoted to self improvement and leading a better life called FLOURIVO TV.I have a logo. We have 3 executives that need cards.I want it to be a heavy stock card: professional but showing our creative nature

Industry/Entity Type

Business

Contact Information for Business Card

CLAUDIA SAENZ AMLIECEO350 San Juan DrPonte Vedra Beach FL 32082904-473-5953

```html
<!DOCTYPE html>
<html lang="en">
<head>
<meta charset="utf-8">
<title>Flourivo TV — Business Card</title>
<link href="https://fonts.googleapis.com/css2?family=Arimo:wght@400;700&display=swap" rel="stylesheet">
<style>
  :root {
    --backdrop: #e7e4df;
    --card: #ffffff;
    --card-shade: #f1f1f1;
    --brand-red: #c4222b;
    --brand-red-dark: #8f1219;
    --ink: #231f20;
  }
  * { margin: 0; padding: 0; box-sizing: border-box; }
  html, body {
    width: 1200px; height: 892px; overflow: hidden;
    background: var(--backdrop);
    font-family: "Arimo", Arial, sans-serif;
  }
  .business-card {
    position: absolute; left: 75px; top: 146px;
    width: 1050px; height: 600px;
    background: linear-gradient(160deg, var(--card) 0%, var(--card-shade) 100%);
    box-shadow: 0 10px 30px rgba(0,0,0,0.18);
    overflow: hidden;
  }
  .brand-band {
    position: absolute; left: 0; top: 0; width: 220px; height: 100%;
    background: linear-gradient(90deg, var(--brand-red-dark) 0%, var(--brand-red) 100%);
  }
  .brand-mark {
    position: absolute; left: 170px; top: 92px;
    width: 100px; height: 100px; border-radius: 50%;
    background: var(--card);
  }
  .brand-name {
    position: absolute; left: 292px; top: 70px;
    font-size: 118px; font-weight: 700; letter-spacing: -2px;
    color: var(--ink); line-height: 1; white-space: nowrap;
  }
  .divider {
    position: absolute; left: 220px; right: 0; top: 262px;
    height: 3px; background: var(--brand-red);
  }
  .person { position: absolute; left: 250px; top: 300px; }
  .person-name {
    font-size: 42px; font-weight: 700; color: var(--brand-red);
    letter-spacing: 0.5px; white-space: nowrap;
  }
  .person-title {
    margin-top: 6px; font-size: 26px; font-weight: 700; color: var(--ink);
  }
  .contact { position: absolute; left: 330px; top: 448px; list-style: none; }
  .contact-item {
    display: flex; align-items: center; gap: 12px;
    font-size: 25px; font-weight: 700; color: var(--ink);
    margin-bottom: 14px; white-space: nowrap;
  }
  .contact-icon { width: 20px; height: 20px; flex: none; }
</style>
</head>
<body>
  <article class="business-card">
    <div class="brand-band"></div>
    <div class="brand-mark"></div>
    <div class="brand-name">flourivo TV</div>
    <div class="divider"></div>

    <div class="person">
      <div class="person-name">Mirella Okafor Dunst</div>
      <div class="person-title">CEO</div>
    </div>

    <ul class="contact">
      <li class="contact-item">
        <svg class="contact-icon" viewBox="0 0 20 20" aria-hidden="true">
          <rect width="20" height="20" fill="#231f20"/>
          <path d="M6 4h3l1 4-2 1a7 7 0 0 0 3 3l1-2 4 1v3a2 2 0 0 1-2 2A11 11 0 0 1 4 6a2 2 0 0 1 2-2z" fill="#fff"/>
        </svg>
        541-618-2047
      </li>
      <li class="contact-item">
        <svg class="contact-icon" viewBox="0 0 20 20" aria-hidden="true">
          <rect width="20" height="20" fill="#231f20"/>
          <path d="M10 3a5 5 0 0 1 5 5c0 4-5 9-5 9s-5-5-5-9a5 5 0 0 1 5-5z" fill="#fff"/>
          <circle cx="10" cy="8" r="2" fill="#231f20"/>
        </svg>
        718 Harlow Creek Dr Larkmoor Springs OR 97390
      </li>
    </ul>
  </article>
</body>
</html>
```